Beer can label design for 12oz cans

we want a clean easy to read label we will be changing the colors to coordinate with the name change of the beer but want everyone to know what they are looking at in regards to the type of beer and us as a brewery. we are in Alaska and i picture a orange red blue green and maybe yellow color to make it clear what beer they are buying. it will be going on a 12oz can. wold like the logo to be 1 color like a dark grey maybe a weatherd look at angle maybe just to give it a little character. needs to have BIG LAKE, AK on the top or the label also needs to have made in alaska somewhere on there. there are lots of rules here are some designs i reallylike also. we are on a lake and look at north americas tallest mountain, Denali Moutain.

Target Market(s)

beer drinkers, want a recognizable can thats easy to decipher the beer type

Industry/Entity Type

drink branding.

Requirements
Must have
• this will be call the "Gold Pax" its a double IPA needs to have the appropriate letter sizes and requirements for a label
Nice to have
• want it to be clean but pop also

```html
<!DOCTYPE html>
<html lang="en">
<head>
<meta charset="utf-8">
<title>Gold Pax Double IPA – Can Label</title>
<link href="https://fonts.googleapis.com/css2?family=Alfa+Slab+One&family=Montserrat:wght@300;400;800&family=Oswald:wght@300;500;600&display=swap" rel="stylesheet">
<style>
  :root{
    --navy:#1f3a5c;
    --navy-deep:#1c3150;
    --panel:#c6deea;
    --lake:#7cbfd4;
    --white:#ffffff;
    --stone:#9a9a9a;
  }
  *{margin:0;padding:0;box-sizing:border-box}
  html,body{width:1200px;height:562px;overflow:hidden;background:var(--white)}
  .label{position:relative;width:1200px;height:562px;font-family:"Oswald",sans-serif;color:var(--navy)}
  .label p,.label h3{position:absolute}

  /* side panels */
  .panel{position:absolute;top:0;width:257px;height:562px;background:var(--panel)}
  .panel--story{left:0}
  .panel--legal{left:943px}

  .brand-name{position:absolute;left:30px;width:201px;top:44px;text-align:center;font-weight:600;color:var(--navy)}
  .brand-name .main{display:block;font-size:31px;line-height:32px;letter-spacing:3px}
  .brand-name .sub{display:block;font-size:18px;line-height:20px;letter-spacing:3px}

  .body-text{font-weight:300;font-size:14px;line-height:20px;letter-spacing:-.1px;color:var(--navy)}
  .heading{font-weight:500;font-size:14px;line-height:20px}

  .story{left:30px;top:118px;width:201px;text-align:justify}
  .ingredients-heading{left:30px;top:322px}
  .ingredients{left:30px;top:342px;width:205px}
  .brewer-heading{left:30px;top:407px}
  .brewer{left:30px;top:427px;width:215px;white-space:nowrap;letter-spacing:-.3px}

  /* centre artwork */
  .front{position:absolute;left:257px;top:0;width:686px;height:562px;background:var(--white);overflow:hidden;text-align:center}
  .front > *{position:absolute;left:0;right:0}
  .front-town{top:29px;font-family:"Montserrat",sans-serif;font-weight:800;font-size:27px;line-height:32px;letter-spacing:6px;color:var(--navy)}
  .scene{left:0;top:72px;width:686px;height:297px;background:linear-gradient(180deg,#eef5f9 0%,#c3dae7 28%,#94b6cc 50%,#33527a 70%,var(--navy-deep) 100%)}
  .scene-brand{top:176px;display:flex;align-items:center;justify-content:center;gap:12px;font-family:"Oswald",sans-serif;font-weight:600;font-size:44px;line-height:50px;letter-spacing:2px;color:var(--stone)}
  .scene-brand .dot{width:20px;height:20px;border-radius:50%;background:var(--stone)}
  .made-in{top:333px;font-family:"Montserrat",sans-serif;font-weight:800;font-size:25px;line-height:30px;letter-spacing:5px;color:var(--white)}
  .lake{top:369px;height:193px;background:var(--lake)}
  .beer-name{top:370px;font-family:"Alfa Slab One",serif;font-weight:400;font-size:80px;line-height:84px;color:var(--white);letter-spacing:1px}
  .beer-style{top:446px;font-family:"Montserrat",sans-serif;font-size:38px;line-height:42px;color:var(--navy)}
  .beer-style .thin{font-weight:300}
  .beer-style .bold{font-weight:800}
  .beer-stats{top:500px;font-family:"Montserrat",sans-serif;font-weight:400;font-size:16px;line-height:20px;color:var(--white);letter-spacing:.5px}

  /* legal side */
  .warning-title{left:29px;top:38px;text-transform:uppercase}
  .warning{left:29px;top:59px;width:201px;text-transform:uppercase;text-align:justify;text-align-last:justify;letter-spacing:-.1px}
  .warning .last{display:block;text-align-last:left}
  .best-before{left:30px;top:281px}
  .code-box{position:absolute;left:30px;top:315px;width:199px;height:138px;background:var(--white)}
  .recycle{position:absolute;left:29px;top:483px;width:200px;display:flex;align-items:center;justify-content:space-between}
  .recycle svg{width:44px;height:42px}
  .recycle-text{font-weight:500;font-size:14px;letter-spacing:.1px}
</style>
</head>
<body>
<div class="label">

  <section class="panel panel--story">
    <div class="brand-name"><span class="main">TALLWATER</span><span class="sub">BREWING</span></div>
    <p class="body-text story">Alaskan IPA is a bold and hoppy beer that captures the unique flavors of the Last Frontier. Brewed with local ingredients and techniques, this beer features a distinct hop profile with hints of citrus, pine, and floral notes. The crisp, clean water of Alaska adds a refreshing finish to this deliciously refreshing IPA.</p>
    <h3 class="heading ingredients-heading">INGREDIENTS:</h3>
    <p class="body-text ingredients">Water, Base Malt, Caramel Malt,<br>Hops, Yeast</p>
    <h3 class="heading brewer-heading">BREWED AND CANNED BY:</h3>
    <p class="body-text brewer">TALLWATER BREWING COMPANY, LLC<br>4880 N Shoreline Rd, Big Lake, AK 99652,<br>United States<br>Phone: +1 907-555-0142<br>www.tallwaterbrewing.com</p>
  </section>

  <section class="front">
    <div class="front-town">BIG LAKE, AK</div>
    <div class="scene" role="img" aria-label="Illustration of snow-capped Alaskan mountains above a dark evergreen forest"></div>
    <div class="scene-brand"><span class="dot"></span>TALLWATER BREWING</div>
    <div class="made-in">Made in Alaska</div>
    <div class="lake"></div>
    <h1 class="beer-name">GOLD PAX</h1>
    <div class="beer-style"><span class="thin">DOUBLE </span><span class="bold">IPA</span></div>
    <div class="beer-stats">6.2% ALC. BY VOL. | 50 IBU<br>CONTENTS 12 FL.OZ</div>
  </section>

  <section class="panel panel--legal">
    <p class="heading warning-title">Government Warning:</p>
    <p class="body-text warning">(1) According to the Surgeon General, women should not drink alcoholic beverages during pregnancy because of the risk of birth defects. (2) Consumption of alcoholic beverages impairs your ability to drive a car or operate machinery, and may cause <span class="last">health problems.</span></p>
    <p class="heading best-before">Best Before:</p>
    <div class="code-box"></div>
    <div class="recycle">
      <svg viewBox="0 0 44 42" aria-hidden="true">
        <g fill="none" stroke="var(--navy)" stroke-width="5" stroke-linejoin="round">
          <path d="M14 12 L21 3 L28 12"/>
          <path d="M35 20 L41 31 L31 37"/>
          <path d="M13 37 L3 31 L9 20"/>
        </g>
        <g fill="var(--navy)">
          <polygon points="25,8 34,9 30,17"/>
          <polygon points="27,40 20,35 27,30"/>
          <polygon points="3,25 6,16 13,22"/>
        </g>
      </svg>
      <span class="recycle-text">PLEASE RECYCLE THIS CAN</span>
    </div>
  </section>

</div>
</body>
</html>
```